Brightwell Controls - ELectrical Contractor Van Wrap

Looking for a new, modernized logo for our new van fleet. (2023 Harlow Courier Full Size)
Brightwell Controls is an electrical contractor in Seattle, focusing on Commercial Electrical, Fire & Security installation, service & inspections. We would like to stick with white/black/grey/red as the color scheme. I added our logo & an image of our current small vans. I do not want them to match perfectly, but be similar. I am not opposed to getting rid of the Flame/Red Circle

Target Market(s)

Commercial Property Management groups/ Apartment Properties

Industry/Entity Type

Electrical

Colors
EB3D1F
EC4F4E
F09395
F8D3D4
FCEDEE

Requirements
Nice to have
• Modern/simplistic

```html
<!DOCTYPE html>
<html lang="en">
<head>
<meta charset="utf-8">
<title>Brightwell Controls – Fleet Wrap Side</title>
<link rel="stylesheet" href="https://fonts.googleapis.com/css2?family=Roboto+Condensed:wght@300;400;700&display=swap">
<style>
  :root {
    --page-bg: #f2f2f2;
    --wrap-light: #e4e5e7;
    --wrap-mid: #d2d4d7;
    --ink: #222222;
    --brand-red: #d71c24;
  }
  * { margin: 0; padding: 0; box-sizing: border-box; }
  html, body { width: 1200px; height: 597px; overflow: hidden; }
  body {
    position: relative;
    background: var(--page-bg);
    font-family: "Roboto Condensed", "Arial Narrow", sans-serif;
    color: var(--ink);
  }
  .circuit-texture {
    position: absolute;
    left: 260px; top: 118px;
    width: 680px; height: 360px;
    background: linear-gradient(180deg, var(--wrap-light), var(--wrap-mid));
    border-radius: 6px;
  }
  .wrap-artwork {
    position: absolute;
    left: 333px; top: 170px;
    width: 534px; height: 256px;
  }
  .wordmark {
    position: absolute;
    left: 39px; top: 42px;
    width: 262px;
    text-align: right;
    line-height: 1;
    white-space: nowrap;
  }
  .wordmark-top {
    display: block;
    font-weight: 300;
    font-size: 52px;
    letter-spacing: -1px;
  }
  .wordmark-bottom {
    display: block;
    font-weight: 700;
    font-size: 60px;
    letter-spacing: -1px;
    margin-top: 4px;
  }
  .brand-lockup {
    position: absolute;
    left: 320px; top: 0;
    width: 214px; height: 210px;
    display: flex;
    flex-direction: column;
    align-items: center;
    justify-content: center;
    gap: 12px;
  }
  .brand-dot {
    width: 120px; height: 120px;
    border-radius: 50%;
    background: var(--brand-red);
  }
  .brand-name {
    color: var(--brand-red);
    font-weight: 700;
    font-size: 22px;
    text-align: center;
    line-height: 1.05;
    text-transform: uppercase;
  }
  .service-line {
    position: absolute;
    left: 0; top: 228px;
    display: flex;
    align-items: center;
    gap: 12px;
    list-style: none;
    white-space: nowrap;
  }
  .service {
    display: flex;
    align-items: center;
    gap: 4px;
    font-weight: 300;
    font-size: 29px;
    line-height: 1;
  }
  .service-marker {
    width: 20px; height: 20px;
    border-radius: 50%;
    background: var(--brand-red);
  }
</style>
</head>
<body>
  <div class="circuit-texture" role="img" aria-label="Faint grey circuit-board line pattern across the van side"></div>

  <div class="wrap-artwork">
    <h1 class="wordmark">
      <span class="wordmark-top">BRIGHTWELL</span>
      <span class="wordmark-bottom">CONTROLS</span>
    </h1>

    <div class="brand-lockup">
      <span class="brand-dot"></span>
      <span class="brand-name">Brightwell<br>Controls</span>
    </div>

    <ul class="service-line">
      <li class="service"><span class="service-marker"></span>ELECTRICAL</li>
      <li class="service"><span class="service-marker"></span>FIRE</li>
      <li class="service"><span class="service-marker"></span>SECURITY</li>
    </ul>
  </div>
</body>
</html>
```